Business Card for Bloom Vitality & Strength

Hi can you please design a business card with my logo and program logo (the new one I just sent) somewhere on it too maybe on the back? Needs to be eye catching and super cool.
Trudy Melcombe, Director
Master Personal Trainer & Nutrition Coach
0472 816 305
Www.bloomvitalitystrength.com.au
Insta (logo) bloom_vitality_strength #bloomyou7x72018

Target Market(s)

30+ women looking to change lifestyle to healthy mind body etc

Industry/Entity Type

Health And Wellness

Contact Information for Business Card

As above

Font styles to use
Sans Serif

Colors

Designer to choose colors to be used in the design.

Requirements
Must have
• Must super cool and edgy with a bit of cuteness

```html
<!DOCTYPE html>
<html lang="en">
<head>
<meta charset="utf-8">
<title>Bloom Vitality &amp; Strength – Business Card</title>
<link rel="stylesheet" href="https://fonts.googleapis.com/css2?family=Montserrat:wght@800&family=Questrial&family=Dancing+Script:wght@600&family=Open+Sans:wght@400&display=swap">
<style>
  :root {
    --page-bg: #e6e8e6;
    --card-bg: #f4f5f2;
    --brand-green: #2f9a5d;
    --brand-green-dark: #237a49;
    --frame-green: #2e8f55;
    --ink-grey: #5b5d61;
    --ink-dark: #2b2d30;
    --on-green: #f3f7f2;
    --on-green-soft: rgba(240, 246, 240, 0.82);
    --accent-red: #c8262b;
  }
  * { margin: 0; padding: 0; box-sizing: border-box; }
  html, body {
    width: 1200px;
    height: 899px;
    overflow: hidden;
    background: var(--page-bg);
  }
  .canvas {
    position: relative;
    width: 1200px;
    height: 899px;
  }
  .card {
    position: absolute;
    left: 100px;
    top: 165px;
    width: 1000px;
    height: 570px;
    background: var(--card-bg);
    overflow: hidden;
    box-shadow: 0 10px 30px rgba(0, 0, 0, 0.12);
  }
  .card__shape {
    position: absolute;
    inset: 0;
    width: 1000px;
    height: 570px;
  }
  .brand {
    position: absolute;
    left: 66px;
    top: 78px;
    display: flex;
    align-items: center;
    gap: 14px;
  }
  .brand__dot {
    width: 22px;
    height: 22px;
    border-radius: 50%;
    background: var(--accent-red);
  }
  .brand__name {
    font-family: 'Montserrat', sans-serif;
    font-weight: 800;
    font-size: 27px;
    line-height: 1.1;
    letter-spacing: 0.5px;
    color: var(--ink-dark);
    text-transform: uppercase;
  }
  .person {
    position: absolute;
    left: 50px;
    top: 205px;
    width: 395px;
  }
  .person__name {
    font-family: 'Questrial', sans-serif;
    font-size: 58px;
    line-height: 1;
    color: var(--ink-grey);
    white-space: nowrap;
  }
  .person__role {
    margin-top: 14px;
    text-align: right;
    font-family: 'Open Sans', sans-serif;
    font-size: 19px;
    letter-spacing: 4px;
    color: var(--ink-dark);
  }
  .title {
    position: absolute;
    left: 560px;
    top: 102px;
    width: 400px;
    font-family: 'Dancing Script', cursive;
    font-weight: 600;
    font-size: 46px;
    line-height: 57px;
    color: var(--on-green);
  }
  .title__line { display: block; white-space: nowrap; }
  .title__line--first { padding-left: 100px; }
  .contact {
    position: absolute;
    left: 540px;
    top: 290px;
    list-style: none;
    font-family: 'Open Sans', sans-serif;
    font-size: 19px;
    color: var(--on-green-soft);
  }
  .contact__item {
    display: flex;
    align-items: center;
    gap: 14px;
    height: 36px;
    white-space: nowrap;
  }
  .contact__icon {
    width: 18px;
    height: 18px;
    flex: none;
  }
</style>
</head>
<body>
<main class="canvas">
  <article class="card">
    <svg class="card__shape" viewBox="0 0 1000 570" aria-hidden="true">
      <defs>
        <linearGradient id="greenFill" x1="0" y1="0" x2="1" y2="1">
          <stop offset="0" stop-color="#34a565"/>
          <stop offset="1" stop-color="#237a49"/>
        </linearGradient>
      </defs>
      <path d="M650 0 C540 60 480 190 495 300 C508 420 560 520 625 570 L1000 570 L1000 0 Z" fill="url(#greenFill)"/>
      <rect x="3" y="3" width="994" height="564" fill="none" stroke="var(--frame-green)" stroke-width="6"/>
    </svg>

    <header class="brand">
      <span class="brand__dot"></span>
      <span class="brand__name">Bloom Vitality<br>&amp; Strength</span>
    </header>

    <section class="person">
      <h1 class="person__name">Trudy Melcombe</h1>
      <p class="person__role">DIRECTOR</p>
    </section>

    <h2 class="title">
      <span class="title__line title__line--first">Master</span>
      <span class="title__line">Personal Trainer</span>
      <span class="title__line">&amp; Nutrition Coach</span>
    </h2>

    <ul class="contact">
      <li class="contact__item">
        <svg class="contact__icon" viewBox="0 0 24 24" aria-hidden="true">
          <path fill="currentColor" d="M6.6 10.8a15.1 15.1 0 0 0 6.6 6.6l2.2-2.2a1 1 0 0 1 1-.25 11.4 11.4 0 0 0 3.6.57 1 1 0 0 1 1 1V20a1 1 0 0 1-1 1A17 17 0 0 1 3 4a1 1 0 0 1 1-1h3.5a1 1 0 0 1 1 1c0 1.25.2 2.45.57 3.6a1 1 0 0 1-.25 1z"/>
        </svg>
        <span>0472 816 305</span>
      </li>
      <li class="contact__item">
        <svg class="contact__icon" viewBox="0 0 24 24" aria-hidden="true">
          <circle cx="12" cy="12" r="9" fill="none" stroke="currentColor" stroke-width="2"/>
          <path d="M3 12h18M12 3c3 3 3 15 0 18M12 3c-3 3-3 15 0 18" fill="none" stroke="currentColor" stroke-width="1.6"/>
        </svg>
        <span>www.bloomvitalitystrength.com.au</span>
      </li>
      <li class="contact__item">
        <svg class="contact__icon" viewBox="0 0 24 24" aria-hidden="true">
          <circle cx="12" cy="12" r="8" fill="currentColor"/>
        </svg>
        <span>bloom_vitality_strength #bloomyou7x72018</span>
      </li>
    </ul>
  </article>
</main>
</body>
</html>
```